RESIDENTIAL CONSTRUCTION

We are a company that specializes in building custom residential homes, the design should also emphasize that quality and service is our priority.

Industry/Entity Type

Construction Company

Contact Information for Business Card

Contact Person: Tobias Kerrigan
Company Address: 243 West 9th St San Jose , Ca 95387
Phone Number : 408-736-2049
Email Address: Stonegatecrafts517@mailbrook.net

Font styles to use
Sans Serif

Colors
ec1f27

Requirements
Must have
• CSLB # 2736159
Nice to have
• needs to have same color as logo i uploaded, we will be printing these on a clear plastic card.

```html
<!DOCTYPE html>
<html lang="en">
<head>
<meta charset="utf-8">
<title>Stonegate Crafts – Business Card</title>
<link href="https://fonts.googleapis.com/css2?family=Roboto:wght@400;500;700&display=swap" rel="stylesheet">
<style>
  :root {
    --brand-red: #ec1f27;
    --panel-red: #c02730;
    --deep-red: #8e1a20;
    --tab-black: #141416;
    --card-clear: #f3f5f7;
    --card-edge: #d5dbe1;
    --backdrop: #e4e8ec;
    --text-light: #f4f4f4;
    --rule: #c9ced6;
  }
  * { margin: 0; padding: 0; box-sizing: border-box; }
  html, body {
    width: 1200px; height: 900px; overflow: hidden;
    background: var(--backdrop);
    font-family: "Roboto", Arial, sans-serif;
  }
  .card {
    position: absolute; left: 75px; top: 150px;
    width: 1050px; height: 598px;
    background: var(--card-clear);
    border: 1px solid var(--card-edge);
    box-shadow: 0 12px 40px rgba(40, 50, 60, 0.15);
    overflow: hidden;
  }
  .card-shapes { position: absolute; inset: 0; width: 100%; height: 100%; }
  .contact-name {
    position: absolute; left: 46px; top: 80px;
    font-size: 31px; font-weight: 500; letter-spacing: 0.5px;
    color: var(--text-light); text-transform: uppercase;
  }
  .contact-line {
    position: absolute; left: 46px;
    font-size: 22px; font-weight: 400; color: var(--text-light);
  }
  .contact-phone { top: 290px; }
  .contact-email { top: 406px; }
  .contact-address { top: 507px; }
  .company-mark {
    position: absolute; left: 571px; top: 288px;
    display: flex; align-items: center; gap: 14px;
  }
  .company-square { width: 30px; height: 30px; background: var(--deep-red); }
  .company-name {
    font-size: 34px; font-weight: 700; letter-spacing: 1px;
    color: var(--deep-red); text-transform: uppercase;
  }
  .license-number {
    position: absolute; right: 57px; top: 532px;
    font-size: 21px; font-weight: 500; color: var(--deep-red);
  }
</style>
</head>
<body>
  <div class="card">
    <svg class="card-shapes" viewBox="0 0 749 427" preserveAspectRatio="none" aria-hidden="true">
      <polygon class="red-panel" points="0,0 316,0 426,427 0,427" fill="var(--panel-red)"/>
      <polygon class="icon-tab" points="294,193 366,193 381,253 309,253" fill="var(--tab-black)"/>
      <polygon class="icon-tab" points="313,269 385,269 401,333 329,333" fill="var(--tab-black)"/>
      <polygon class="icon-tab" points="333,346 405,346 421,408 349,408" fill="var(--tab-black)"/>
      <line class="divider" x1="26" y1="264" x2="405" y2="264" stroke="var(--rule)" stroke-width="2"/>
      <line class="divider" x1="26" y1="336" x2="405" y2="336" stroke="var(--rule)" stroke-width="2"/>
      <!-- phone icon -->
      <g class="icon-phone" fill="#e8e8e8">
        <rect x="328" y="218" width="20" height="6" rx="3"/>
        <rect x="330" y="224" width="16" height="10" rx="2"/>
        <rect x="335" y="227" width="6" height="4" fill="var(--tab-black)"/>
      </g>
      <!-- mail icon -->
      <g class="icon-mail">
        <rect x="347" y="291" width="22" height="15" fill="#e8e8e8"/>
        <polyline points="347,291 358,300 369,291" fill="none" stroke="var(--tab-black)" stroke-width="1.6"/>
      </g>
      <!-- pin icon -->
      <g class="icon-pin">
        <polygon points="362,374 384,374 388,382 358,382" fill="#e8e8e8"/>
        <path d="M373 358 a6 6 0 0 1 6 6 c0 5 -6 10 -6 10 c0 0 -6 -5 -6 -10 a6 6 0 0 1 6 -6z" fill="#e8e8e8"/>
        <circle cx="373" cy="364" r="2.2" fill="var(--tab-black)"/>
      </g>
    </svg>

    <div class="contact-name">Tobias Kerrigan</div>
    <div class="contact-line contact-phone">408-736-2049</div>
    <div class="contact-line contact-email">Stonegatecrafts517@mailbrook.net</div>
    <div class="contact-line contact-address">243 West 9th St San Jose , Ca 95387</div>

    <div class="company-mark">
      <span class="company-square"></span>
      <span class="company-name">Stonegate Crafts</span>
    </div>

    <div class="license-number">CSLB # 2736159</div>
  </div>
</body>
</html>
```